Derya & Kerem Wedding Invitation and Decorative Designs

We are looking for a sweet and elegant design for our wedding invitation. We need different versions of the same design to use both as printed hard copies and in digital formats (WhatsApp image, instagram post, etc) Please see attached sample invitation, which we like as a simple and elegant option, but also find it quite basic. We are open to creative suggestions following a similar style.
Once we decide on an invitation design, we would like to use the same design elements in guest name cards, welcome sign, menu cards and print cover for the dance floor of our wedding venue. Please see random samples of these materials attached. We also attach a photo from our wedding venue displaying a close to final visual of the decoration we chose for our wedding day (sharing in case it helps as an inspiration source and helps with matching decoration colors with the designs)
Requirements
Must have
- Must have a style similar to the attached sample invitation

```html
<!DOCTYPE html>
<html lang="tr">
<head>
<meta charset="utf-8">
<title>Derya &amp; Kerem — Düğün Davetiyesi</title>
<link href="https://fonts.googleapis.com/css2?family=Great+Vibes&family=EB+Garamond:wght@400;500&family=Montserrat:wght@400;500;600&display=swap" rel="stylesheet">
<style>
  :root{
    --page-bg:#e7ddd6;
    --card:#fbfcfa;
    --ink:#4a3a33;
    --ink-soft:#6b5a50;
    --sage:#aec49c;
    --sage-wash:#dce8e0;
    --leaf:#5f9a5e;
    --rose:#f1c3c8;
    --peach:#f3c8a8;
    --gold:#d8b266;
  }
  *{margin:0;padding:0;box-sizing:border-box}
  html,body{width:1200px;height:1200px;overflow:hidden;background:var(--page-bg)}
  .invitation{
    position:absolute;left:200px;top:30px;width:800px;height:1140px;
    background:radial-gradient(ellipse at 70% 60%,var(--sage-wash) 0%,rgba(220,232,224,0) 55%),var(--card);
    box-shadow:0 10px 30px rgba(80,60,50,.18);
    overflow:hidden;
    color:var(--ink);
  }
  .floral{position:absolute}
  .floral--top{right:-40px;top:-40px;width:380px;height:520px;
    background:radial-gradient(circle at 45% 15%,var(--rose) 0 22%,transparent 40%),
               radial-gradient(circle at 85% 35%,var(--peach) 0 14%,transparent 28%),
               radial-gradient(ellipse at 60% 55%,rgba(95,154,94,.55) 0 25%,transparent 55%);
    border-bottom-left-radius:70%}
  .floral--bottom{left:-40px;bottom:-40px;width:560px;height:480px;
    background:radial-gradient(circle at 50% 75%,var(--rose) 0 18%,transparent 34%),
               radial-gradient(circle at 12% 55%,var(--peach) 0 12%,transparent 26%),
               radial-gradient(ellipse at 30% 40%,rgba(95,154,94,.5) 0 25%,transparent 60%);
    border-top-right-radius:70%}
  .greeting{position:absolute;top:190px;left:80px;width:560px;text-align:center;
    font-family:"EB Garamond",serif;font-size:30px;line-height:1.25;color:var(--ink-soft)}
  .names{position:absolute;top:300px;left:0;width:800px;text-align:center;font-family:"Great Vibes",cursive;color:var(--ink)}
  .names .name{display:block;font-size:104px;line-height:1.1}
  .names .amp{display:block;font-family:"EB Garamond",serif;font-size:52px;margin:6px 0 14px}
  .date{position:absolute;top:665px;left:0;width:800px;display:flex;justify-content:center;align-items:flex-end;gap:22px;font-family:"Montserrat",sans-serif}
  .date .side{font-size:18px;letter-spacing:3px;padding-bottom:10px}
  .date .bar{width:1px;height:40px;background:var(--ink);margin-bottom:8px}
  .date .day{text-align:center;font-family:"EB Garamond",serif;font-size:30px;font-weight:500;line-height:1}
  .date .day b{display:block;font-family:"Montserrat",sans-serif;font-size:54px;font-weight:600}
  .invited{position:absolute;top:790px;width:800px;text-align:center;font-family:"Montserrat",sans-serif;font-size:48px;font-weight:500;color:var(--ink)}
  .venue{position:absolute;top:865px;width:800px;text-align:center;font-family:"EB Garamond",serif;font-size:22px;line-height:1.35}
  .schedule{position:absolute;top:950px;left:110px;display:flex;gap:12px}
  .slot{width:140px;height:130px;border-radius:12px;background:var(--sage);display:flex;flex-direction:column;align-items:center;justify-content:center;gap:12px;font-family:"Montserrat",sans-serif;font-size:24px;color:var(--ink)}
  .slot svg{width:46px;height:46px;stroke:var(--ink);fill:none;stroke-width:2.4;stroke-linecap:round}
  .contact{position:absolute;right:70px;top:1095px;font-family:"EB Garamond",serif;font-size:20px}
</style>
</head>
<body>
<main class="invitation">
  <div class="floral floral--top" role="img" aria-label="Watercolour roses and green leaves"></div>
  <div class="floral floral--bottom" role="img" aria-label="Watercolour roses and green leaves"></div>

  <p class="greeting">Bu mutlu günümüzde sizleri de aramızda<br>görmekten mutluluk duyacağız.</p>

  <h1 class="names">
    <span class="name">Derya</span>
    <span class="amp">&amp;</span>
    <span class="name">Kerem</span>
  </h1>

  <div class="date">
    <span class="side">Ağustos</span>
    <span class="bar"></span>
    <span class="day">Pazar<b>24</b></span>
    <span class="bar"></span>
    <span class="side">2024</span>
  </div>

  <h2 class="invited">DAVETLİSİNİZ</h2>
  <p class="venue">LİMAN BAHÇE: Çınaraltı Sok. No: 14<br>Kuzeykent, İstanbul</p>

  <div class="schedule">
    <div class="slot">
      <svg viewBox="0 0 48 48"><path d="M6 10h16l-8 12zM14 22v14M9 36h10M26 10h16l-8 12zM34 22v14M29 36h10"/></svg>18.00
    </div>
    <div class="slot">
      <svg viewBox="0 0 48 48"><circle cx="18" cy="28" r="10"/><circle cx="30" cy="28" r="10"/><path d="M15 14l3-5 3 5M27 14l3-5 3 5"/></svg>19.00
    </div>
    <div class="slot">
      <svg viewBox="0 0 48 48"><circle cx="24" cy="24" r="13"/><circle cx="24" cy="24" r="8"/><path d="M5 8v10M8 8v10M5 18h3M6.5 18v22M43 8c-4 2-4 10 0 12v20"/></svg>20.00
    </div>
    <div class="slot">
      <svg viewBox="0 0 48 48"><path d="M8 40l8-22 14 14z"/><path d="M26 20l8-10M30 26l10-2M22 16l-2-8M36 6l2 2M42 14l2 2"/></svg>00.00
    </div>
  </div>

  <p class="contact">LCV: 02125550147</p>
</main>
</body>
</html>
```